Stationery for Software Developer
Glen Ambrose
Project: Stationery for Software Developer
Stationery for Software Developer - Information Technology
Creative Brief
Professional
Software Engineer
Greater Seattle Area
glen@ambrosk.me
http://ambrosk.me
Chirpline: @ambrog Circlr+: +GlenAmbrose Facepage: gambrosk WorkNexus: glenambrose (Prefer Social Icons to be used instead of the names)
Main Logo with name on front. Open to variations of the main logo on front.
sevensky sevensky
gambrosk gambrosk
My apologies. I accidentally started this project before I had my logo in hand. I have contacted support about suspending this contest for 4 days until I have it. Thanks for the interest! Glen
paul1990 paul1990
Hi, Where is your logo?

```html
<!DOCTYPE html>
<html lang="en">
<head>
<meta charset="utf-8">
<title>Glen Ambrose – Business Cards</title>
<link href="https://fonts.googleapis.com/css2?family=Open+Sans:wght@400;600;700&display=swap" rel="stylesheet">
<style>
  :root {
    --backdrop: #2b2b2d;
    --card-light: #ffffff;
    --card-shade: #e9eaec;
    --slate: #4d6079;
    --pink: #d84b93;
    --ink: #34506e;
    --muted: #6c737c;
    --mark: #5f8fb0;
  }
  * { margin: 0; padding: 0; box-sizing: border-box; }
  html, body { width: 1200px; height: 693px; overflow: hidden; }
  body {
    background: var(--backdrop);
    font-family: "Open Sans", Arial, sans-serif;
    position: relative;
  }
  .card {
    position: absolute;
    width: 498px;
    height: 284px;
    border-radius: 24px;
    overflow: hidden;
    background: radial-gradient(ellipse at 60% 35%, var(--card-light) 40%, var(--card-shade) 100%);
  }
  .card--front { left: 212px; top: 29px; }
  .card--back { left: 474px; top: 334px; }

  .side-band { position: absolute; left: 0; top: 0; width: 498px; height: 284px; }

  .brand {
    position: absolute;
    display: flex;
    align-items: center;
    color: var(--ink);
    font-weight: 400;
    white-space: nowrap;
  }
  .brand__square { display: inline-block; background: var(--mark); }
  .card--front .brand { left: 125px; top: 70px; font-size: 35px; transform: translateY(-50%); }
  .card--front .brand__square { width: 40px; height: 40px; margin-right: 14px; }

  .holder { position: absolute; left: 126px; top: 118px; }
  .holder__name { font-size: 22px; font-weight: 700; color: var(--ink); line-height: 1.1; }
  .holder__role { font-size: 14px; color: var(--muted); margin-top: 4px; }

  .contacts { position: absolute; left: 126px; top: 183px; list-style: none; }
  .contacts li {
    display: flex; align-items: center;
    font-size: 12px; color: var(--muted);
    height: 18.5px;
  }
  .contacts svg { width: 12px; height: 12px; margin-right: 8px; fill: var(--ink); }

  .card--back .brand {
    left: 0; right: 0; top: 100px;
    flex-direction: column;
    font-size: 34px;
  }
  .card--back .brand__square { width: 44px; height: 44px; margin-bottom: 20px; }
</style>
</head>
<body>
  <section class="card card--front">
    <svg class="side-band" viewBox="0 0 498 284" aria-hidden="true">
      <path d="M0 0 H30 C95 60 60 170 120 284 H0 Z" fill="var(--slate)"/>
      <path d="M30 0 H52 C112 70 80 170 140 284 H120 C60 170 95 60 30 0 Z" fill="var(--pink)"/>
    </svg>
    <div class="brand"><span class="brand__square"></span>Glen Ambrose</div>
    <div class="holder">
      <p class="holder__name">Dale Corvin</p>
      <p class="holder__role">Founder</p>
    </div>
    <ul class="contacts">
      <li><svg viewBox="0 0 12 12"><path d="M3 0h6a1 1 0 0 1 1 1v10a1 1 0 0 1-1 1H3a1 1 0 0 1-1-1V1a1 1 0 0 1 1-1zm0 1.5v8h6v-8zm3 8.8a.6.6 0 1 0 0 1.2.6.6 0 0 0 0-1.2z"/></svg>206 555 0148</li>
      <li><svg viewBox="0 0 12 12"><path d="M0 2h12v8H0zm1 1v.4l5 3.3 5-3.3V3zm0 1.6V9h10V4.6L6 7.9z"/></svg>glen@ambrosk.me</li>
      <li><svg viewBox="0 0 12 12"><path d="M6 0a6 6 0 1 1 0 12A6 6 0 0 1 6 0zm0 1a5 5 0 1 0 0 10A5 5 0 0 0 6 1zm-.5 1v3.5H2v1h3.5V10h1V6.5H10v-1H6.5V2z"/></svg>http://ambrosk.me</li>
      <li><svg viewBox="0 0 12 12"><circle cx="6" cy="6" r="5"/></svg>@ambrog</li>
    </ul>
  </section>

  <section class="card card--back">
    <div class="brand"><span class="brand__square"></span>Glen Ambrose</div>
  </section>
</body>
</html>
```